Design a poster that illustrates the six central pillars of our school district's efforts with students. The attached PDF outlines the six main competencies we aim for students to possess upon graduation. Each of the 6 has 3 bullet points for the poster as well. The title is "Profile of a Drifter". Our mascot is this attached winged wheel. The overall concept is that staff take kids when they are young and develop these 6 things when they graduate. Our colors are navy, red, and white. We will make this poster in a variety of sizes in offices, classrooms, and in digital spaces as well. On the PDF - ignore the column that says "Synthesis". That has nothing to do with this poster.

The district is Corvath Falls Public Schools https://www.corvath.k12.example.us/

```html
<!DOCTYPE html>
<html lang="en">
<head>
<meta charset="utf-8">
<title>Profile of a Drifter</title>
<link rel="stylesheet" href="https://fonts.googleapis.com/css2?family=Oswald:wght@400;500;600&display=swap">
<style>
:root{
  --navy:#0c1a5e;
  --navy-deep:#0a1449;
  --red:#a3161c;
  --white:#ffffff;
  --ink:#0e1330;
  --backdrop:#e4e6e9;
}
*{margin:0;padding:0;box-sizing:border-box}
html,body{width:1200px;height:1001px;overflow:hidden;background:var(--backdrop)}
.poster{
  position:absolute;left:264px;top:28px;width:666px;height:943px;
  background:var(--white);overflow:hidden;
  font-family:"Oswald",sans-serif;color:var(--ink);
  box-shadow:0 2px 10px rgba(0,0,0,.12);
}
.poster svg.art{position:absolute;left:0;top:0}
.title{
  position:absolute;right:53px;top:42px;text-align:right;
  color:var(--white);font-weight:500;font-size:56px;line-height:54px;letter-spacing:.5px;
  text-transform:uppercase;
}
.subtitle{
  position:absolute;right:53px;top:160px;color:var(--white);
  font-size:12.5px;font-weight:500;letter-spacing:.3px;text-transform:uppercase;
}
.mascot-name{
  position:absolute;left:130px;top:112px;width:150px;text-align:center;
  color:var(--white);font-size:26px;font-weight:500;text-transform:uppercase;
}
.pillar-label{
  position:absolute;color:var(--white);font-size:21px;font-weight:500;line-height:32px;
}
.pillar-text{
  position:absolute;left:163px;font-size:12px;line-height:16.5px;font-weight:400;
  color:var(--ink);
}
.url{
  position:absolute;right:82px;top:872px;color:var(--red);
  font-size:34px;font-weight:500;
}
</style>
</head>
<body>
<main class="poster">
  <svg class="art" width="666" height="943" viewBox="0 0 666 943" aria-hidden="true">
    <!-- header band -->
    <polygon points="0,0 666,0 666,240 505,222 0,222" fill="var(--navy)"/>
    <polygon points="0,222 150,150 505,222" fill="var(--white)"/>
    <polygon points="0,222 0,60 150,150" fill="var(--navy-deep)"/>
    <polygon points="60,50 520,200 505,222 40,72" fill="var(--red)"/>
    <circle cx="205" cy="125" r="52" fill="var(--navy)" stroke="var(--white)" stroke-width="3"/>

    <!-- connectors -->
    <g fill="none" stroke="var(--navy)" stroke-width="1.5">
      <polyline points="320,262 113,262 113,317"/>
      <polyline points="350,364 555,364 555,419"/>
      <polyline points="290,466 113,466 113,519"/>
      <polyline points="350,566 545,566 545,619"/>
      <polyline points="335,667 113,667 113,719"/>
    </g>

    <!-- label bars -->
    <g fill="var(--red)">
      <polygon points="320,246 515,246 515,279 335,279"/>
      <polygon points="150,348 350,348 335,380 150,380"/>
      <polygon points="290,450 515,450 515,482 305,482"/>
      <polygon points="150,551 350,551 335,583 150,583"/>
      <polygon points="335,651 515,651 515,683 350,683"/>
      <polygon points="150,751 365,751 350,783 150,783"/>
    </g>

    <!-- pillar circles -->
    <g fill="var(--navy)" stroke="var(--red)" stroke-width="5">
      <circle cx="556" cy="262" r="48" role="img" aria-label="Icon: head with speech bubble"/>
      <circle cx="111" cy="364" r="48" role="img" aria-label="Icon: head with thinking gears"/>
      <circle cx="556" cy="466" r="48"/>
      <circle cx="111" cy="566" r="48" role="img" aria-label="Icon: chameleon"/>
      <circle cx="556" cy="667" r="48" role="img" aria-label="Icon: handshake"/>
      <circle cx="111" cy="767" r="48" role="img" aria-label="Icon: heart held in a hand"/>
    </g>

    <!-- clipboard with tick -->
    <g fill="none" stroke="var(--white)" stroke-width="2.2" stroke-linecap="round" stroke-linejoin="round">
      <rect x="536" y="438" width="38" height="52" rx="3"/>
      <rect x="547" y="433" width="16" height="8" rx="2"/>
      <line x1="543" y1="452" x2="547" y2="452"/><line x1="551" y1="452" x2="567" y2="452"/>
      <line x1="543" y1="462" x2="547" y2="462"/><line x1="551" y1="462" x2="567" y2="462"/>
      <line x1="543" y1="472" x2="547" y2="472"/><line x1="551" y1="472" x2="560" y2="472"/>
      <circle cx="572" cy="486" r="9" fill="var(--navy)"/>
      <polyline points="567,486 571,490 577,482"/>
    </g>

    <!-- footer band -->
    <polygon points="0,885 380,943 0,943" fill="var(--red)"/>
  </svg>

  <div class="mascot-name">Drifter</div>
  <h1 class="title">Profile<br>of a Drifter</h1>
  <p class="subtitle">The six pillars of Corvath Falls Public Schools</p>

  <div class="pillar-label" style="left:362px;top:246px">Communicator</div>
  <p class="pillar-text" style="top:284px">Expresses ideas clearly and respectfully (written &amp; verbal).<br>Listens actively and understands diverse perspectives.<br>Adjusts communication to suit the audience and context.</p>

  <div class="pillar-label" style="left:180px;top:348px">Critical Thinker</div>
  <p class="pillar-text" style="top:387px">Questions, analyzes, and evaluates information from multiple sources.<br>Identifies and solves complex problems creatively.<br>Uses evidence and diverse perspectives to form reasoned conclusions<br>and make informed decisions</p>

  <div class="pillar-label" style="left:371px;top:450px">Responsible</div>
  <p class="pillar-text" style="top:485px">Takes ownership of actions, choices, and commitments.<br>Manages time, resources, and self to meet expectations.<br>Acts with integrity and advocates for self and others.</p>

  <div class="pillar-label" style="left:182px;top:551px">Adaptable</div>
  <p class="pillar-text" style="top:588px">Responds productively to new situations, challenges, and feedback.<br>Learns from new experiences and applies prior knowledge in evolving contexts.<br>Adjusts behavior and approach to effectively engage with diverse groups<br>and environments.</p>

  <div class="pillar-label" style="left:375px;top:651px">Collaborator</div>
  <p class="pillar-text" style="top:691px">Contributes effectively and cooperatively to shared goals.<br>Listens actively and values diverse ideas and perspectives.<br>Engages respectfully, compromising and leading when appropriate.</p>

  <div class="pillar-label" style="left:182px;top:751px">Compassionate</div>
  <p class="pillar-text" style="top:790px">Understands and acknowledges others' feelings, perspectives, and experiences.<br>Responds with kindness, patience, and support.<br>Seeks to connect with and contribute positively to the well-being of others and<br>the community.</p>

  <div class="url">corvath.k12.example.us</div>
</main>
</body>
</html>
```